We need a Welcome Booklet designed for our Church - Harbourlight Fellowship Church. We would like a design that is contemporary with no religious symbols or old pictures. Please use quality contemporary photos . See attached a Word document with what content we want in the booklet.

Target Market(s)

Guests to the church so new person friendly

Requirements
Must have
• A contemporary modern look
Should not have
• Religious symbols or old pictures

```html
<!DOCTYPE html>
<html lang="en">
<head>
<meta charset="utf-8">
<title>Harbourlight Fellowship Church – Welcome</title>
<link href="https://fonts.googleapis.com/css2?family=Montserrat:wght@400;600&display=swap" rel="stylesheet">
<style>
  :root {
    --ink: #000000;
    --paper: #ffffff;
    --lime: #5e8a1c;
    --olive: #3e4210;
    --plum: #3b1440;
    --lavender: #4a3f8c;
    --chartreuse: #a9b01e;
    --wine: #3a0f33;
    --forest: #1f2a12;
    --ocean: #123a63;
    --violet: #3a2f7a;
    --navy: #0d2440;
    --magenta: #8a1e86;
  }
  html, body {
    margin: 0;
    padding: 0;
    overflow: hidden;
    background: var(--ink);
  }
  .booklet-cover {
    position: relative;
    width: 855px;
    height: 1200px;
    overflow: hidden;
    background: var(--ink);
    font-family: "Montserrat", sans-serif;
    color: var(--paper);
  }
  .photo-tile {
    position: absolute;
  }
  .tile-singers     { left: 0;   top: 0;   width: 315px; height: 240px; background: linear-gradient(160deg, var(--lime), #3f6012); }
  .tile-guitar      { left: 348px; top: 0; width: 334px; height: 90px;  background: linear-gradient(90deg, var(--olive), #5a5f18); }
  .tile-faces       { left: 315px; top: 90px; width: 371px; height: 154px; background: linear-gradient(120deg, var(--plum), #5a1f60); }
  .tile-singer-right{ left: 691px; top: 0;   width: 164px; height: 244px; background: linear-gradient(200deg, #6b62b0, var(--lavender)); }
  .tile-crowd-shirt { left: 0;   top: 423px; width: 343px; height: 146px; background: linear-gradient(150deg, var(--chartreuse), #6e7412); }
  .tile-audience    { left: 0;   top: 569px; width: 343px; height: 136px; background: linear-gradient(90deg, var(--wine), #5a1a50); }
  .tile-speaker     { left: 348px; top: 423px; width: 300px; height: 282px; background: radial-gradient(circle at 45% 40%, #3a4a22, var(--forest)); }
  .tile-smile       { left: 653px; top: 442px; width: 202px; height: 263px; background: linear-gradient(200deg, #1d5a8a, var(--ocean)); }
  .tile-glasses     { left: 0;   top: 705px; width: 320px; height: 235px; background: linear-gradient(160deg, #4c3f96, var(--violet)); }
  .tile-worship     { left: 320px; top: 705px; width: 328px; height: 235px; background: linear-gradient(180deg, #17355a, var(--navy)); }
  .tile-preacher    { left: 653px; top: 705px; width: 202px; height: 235px; background: linear-gradient(200deg, #a42ca0, var(--magenta)); }

  .title-band {
    position: absolute;
    left: 0;
    top: 244px;
    width: 855px;
    height: 179px;
    background: var(--ink);
  }
  .heart-frame {
    position: absolute;
    left: 0;
    top: 0;
    width: 855px;
    height: 1200px;
  }
  .welcome-title {
    position: absolute;
    left: 0;
    width: 828px;
    top: 250px;
    margin: 0;
    text-align: center;
    font-weight: 600;
    font-size: 128px;
    line-height: 160px;
    letter-spacing: -1px;
  }
  .footer-band {
    position: absolute;
    left: 0;
    top: 940px;
    width: 855px;
    height: 260px;
    background: var(--ink);
  }
  .church-name {
    position: absolute;
    left: 61px;
    top: 1000px;
    margin: 0;
    font-weight: 600;
    font-size: 34px;
    line-height: 42px;
  }
  .church-web {
    position: absolute;
    right: 42px;
    top: 1108px;
    margin: 0;
    font-weight: 400;
    font-size: 40px;
    line-height: 50px;
  }
</style>
</head>
<body>
  <main class="booklet-cover">
    <div class="photo-tile tile-singers" role="img" aria-label="Photo of worship singers with microphones, green tint"></div>
    <div class="photo-tile tile-guitar" role="img" aria-label="Photo of hands playing a guitar, olive tint"></div>
    <div class="photo-tile tile-faces" role="img" aria-label="Photo of smiling church members, purple tint"></div>
    <div class="photo-tile tile-singer-right" role="img" aria-label="Photo of a woman singing, lavender tint"></div>
    <div class="photo-tile tile-crowd-shirt" role="img" aria-label="Photo of a congregation member clapping, yellow tint"></div>
    <div class="photo-tile tile-audience" role="img" aria-label="Photo of the congregation seated, wine tint"></div>
    <div class="photo-tile tile-speaker" role="img" aria-label="Photo of a speaker holding a microphone, dark green tint"></div>
    <div class="photo-tile tile-smile" role="img" aria-label="Photo of a smiling woman, blue tint"></div>
    <div class="photo-tile tile-glasses" role="img" aria-label="Photo of a man in worship, violet tint"></div>
    <div class="photo-tile tile-worship" role="img" aria-label="Photo of people during worship, navy tint"></div>
    <div class="photo-tile tile-preacher" role="img" aria-label="Photo of a preacher speaking, magenta tint"></div>

    <div class="title-band"></div>

    <svg class="heart-frame" viewBox="0 0 855 1200" aria-hidden="true">
      <path d="M414 207 C 370 130, 290 88, 205 88 C 95 88, 30 175, 30 275 C 30 375, 85 440, 150 510 L 414 858 L 678 510 C 743 440, 798 375, 798 275 C 798 175, 733 88, 623 88 C 538 88, 458 130, 414 207 Z"
            fill="none" stroke="#ffffff" stroke-width="18" stroke-linejoin="miter"/>
    </svg>

    <h1 class="welcome-title">Welcome</h1>

    <footer class="footer-band"></footer>
    <p class="church-name">Harbourlight<br>Fellowship<br>Church</p>
    <p class="church-web">harbourlight.church</p>
  </main>
</body>
</html>
```